Hoopline Card Design

I have attached a zip folder that has a word document describing everyhing with what I want

Target Market(s)

College basketball coaches and media

Contact Information for Business Card

Everything I want is in the word document in the zip folder

Requirements
Must have
• Must have front back design as described in word document.
Nice to have
• I want it to look sleek and first class. It has to really stand out. I have included a few different logos, the Hoopline.com needs to be on the front and Stridewell.com needs to be on the back side with our contact info. The file I attached has an extensive word document describing everything. I would also like the front with Hoopline.com to be vertical with our twitter handles. Feel free to be creative. and even add a color background. I included PSD files

```html
<!DOCTYPE html>
<html lang="en">
<head>
<meta charset="utf-8">
<title>Hoopline Card Design</title>
<link href="https://fonts.googleapis.com/css2?family=Andika:wght@700&family=Open+Sans:ital,wght@0,400;0,600;0,700;1,700&family=Ubuntu:wght@400;500&display=swap" rel="stylesheet">
<style>
  :root {
    --page: #ecebe8;
    --card: #ffffff;
    --card-back: #f4f4f3;
    --gold: #e6a30c;
    --ink: #4d4d4d;
    --muted: #6a6a6a;
    --blue-top: #12a6dc;
    --blue-mid: #1570bd;
    --blue-deep: #1a3f93;
    --handle-dot: #3cb3e6;
    --stripe-blue: #1a7fc4;
    --stripe-gold: #f0bb12;
  }
  * { margin: 0; padding: 0; box-sizing: border-box; }
  html, body { width: 1200px; height: 1000px; overflow: hidden; background: var(--page); }
  .canvas { position: relative; width: 1200px; height: 1000px; }

  .card {
    position: absolute; top: 252px; width: 295px; height: 503px;
    background: var(--card); overflow: hidden;
    box-shadow: 0 6px 18px rgba(0,0,0,.18);
  }
  .card--front { left: 262px; }
  .card--back { left: 631px; background: var(--card-back); }

  /* Front */
  .front__head { position: absolute; left: 0; top: 0; width: 100%; height: 245px; text-align: center; }
  .brand-name {
    position: absolute; left: 0; right: 0; top: 118px;
    font: 700 31px/1 "Andika", sans-serif; color: var(--gold);
  }
  .tagline {
    position: absolute; left: 0; right: 0; top: 158px;
    font: 700 16.5px/24px "Andika", sans-serif; color: var(--ink);
  }
  .front__panel {
    position: absolute; left: 0; top: 245px; width: 100%; height: 258px;
    background: radial-gradient(ellipse 90% 55% at 50% 0%, var(--blue-top), var(--blue-mid) 55%, var(--blue-deep));
  }
  .handle { position: absolute; left: 28px; display: flex; gap: 11px; color: #fff; font-family: "Ubuntu", sans-serif; }
  .handle__dot { width: 20px; height: 20px; border-radius: 50%; background: var(--handle-dot); margin-top: 2px; flex: none; }
  .handle__name { font-size: 15px; font-weight: 500; line-height: 20px; }
  .handle__mail { font-size: 12.5px; line-height: 16px; }

  /* Back */
  .back__mark {
    position: absolute; left: 10px; top: 14px; height: 330px;
    writing-mode: vertical-rl; transform: rotate(180deg);
    font-family: "Open Sans", sans-serif; color: #6b6b6b;
  }
  .back__name { font-size: 39px; font-weight: 600; line-height: 42px; letter-spacing: -.5px; }
  .back__line { font-size: 10.5px; font-weight: 700; font-style: italic; line-height: 16px; color: #6e6e6e; }
  .back__dot { position: absolute; left: 12px; top: 350px; width: 44px; height: 44px; border-radius: 50%; background: #6b6b6b; }
  .contact {
    position: absolute; right: 30px; top: 357px; text-align: right;
    font-family: "Open Sans", sans-serif; font-size: 12.5px; line-height: 21px; color: var(--muted);
  }
  .contact__name { font-weight: 700; font-size: 13.5px; color: #555; }
  .stripe { position: absolute; bottom: 0; height: 14px; }
  .stripe--blue { left: 0; width: 161px; background: linear-gradient(90deg, #1c6fb2, var(--stripe-blue)); }
  .stripe--gold { left: 174px; right: 0; background: var(--stripe-gold); }
</style>
</head>
<body>
<main class="canvas">
  <section class="card card--front" aria-label="Card front">
    <div class="front__head">
      <div class="brand-name">Hoopline.com</div>
      <p class="tagline">"Following Two-Year College Hoops<br>Closer Than EVER Before"</p>
    </div>
    <div class="front__panel">
      <div class="handle" style="top:62px"><span class="handle__dot"></span><div><div class="handle__name">@DanaMercerHL</div><div class="handle__mail">DanaMercer@Hoopline.com</div></div></div>
      <div class="handle" style="top:118px"><span class="handle__dot"></span><div><div class="handle__name">@CoachRLane</div><div class="handle__mail">rlanehoops@example.com</div></div></div>
      <div class="handle" style="top:170px"><span class="handle__dot"></span><div><div class="handle__name">@CoachTMarsh</div><div class="handle__mail">coach_marsh@example.net</div></div></div>
    </div>
  </section>

  <section class="card card--back" aria-label="Card back">
    <div class="back__mark">
      <div class="back__name">Stridewell.com</div>
      <div class="back__line">"The Recruiter's Guide to Two-Year College Hoops Talent"</div>
    </div>
    <span class="back__dot"></span>
    <div class="contact">
      <div class="contact__name">Dana Mercer</div>
      <div>Director/Owner</div>
      <div>Cell: 555-014-2287</div>
      <div>DanaMercer@Hoopline.com</div>
    </div>
    <span class="stripe stripe--blue"></span>
    <span class="stripe stripe--gold"></span>
  </section>
</main>
</body>
</html>
```